exquisite label design for foam cleanser

Kindly invite you to design bottle label (102 mm*64 mm) for our product, a kind of foam cleanser for wearable aligners. The color of bottle and liquid inside are both clear, but the foam pump is white. You could download the pic of bottle among the uploaded files. I have no KV of our website or posters to supply you, except the logo file attached. Content on the label is attached too. Please check it. I wish the label would make our product look high-end and reliable. And it would be better if you could give some advice on paper material and special requirements for printing, related to your design. I value the texture of label too, because I think that stands for the quality of products. No color limitation for the use of our logo, and please ignore the Chinese characters in our logo, they are not in our plan.
Target Market(s)
16-35 female, orthodontic patients.
Colors
Designer to choose colors to be used in the design.
Look and feel
Each slider illustrates characteristics of the customer's brand and the style your logo design should communicate.

```html
<!DOCTYPE html>
<html lang="en">
<head>
<meta charset="UTF-8">
<title>Feyla Aligner Cleansing Foam – Label</title>
<link href="https://fonts.googleapis.com/css2?family=Montserrat:wght@400;700&family=Noto+Sans+SC:wght@500&family=Yellowtail&display=swap" rel="stylesheet">
<style>
  :root {
    --page: #ffffff;
    --label: #ffffff;
    --label-edge: #e3e8ec;
    --brand-blue: #2fa3d8;
    --band-blue: #2ea4d8;
    --band-shade: #1f8fc4;
    --ink: #222222;
    --white: #ffffff;
    --mint-dark: #137a30;
    --mint: #2a9a3f;
    --leaf: #5dbb4a;
  }
  * { margin: 0; padding: 0; box-sizing: border-box; }
  html, body {
    width: 1200px; height: 985px; overflow: hidden;
    background: var(--page);
  }
  .canvas {
    position: relative; width: 1200px; height: 985px;
    display: flex; align-items: center; justify-content: center;
  }
  .label {
    position: relative; width: 432px; height: 800px;
    background: var(--label);
    border: 1px solid var(--label-edge);
    font-family: 'Montserrat', sans-serif;
    color: var(--ink);
  }
  .brand-name {
    position: absolute; top: 72px; left: 0; width: 100%;
    text-align: center;
    font-family: 'Montserrat', sans-serif;
    font-weight: 700; font-size: 92px; line-height: 1;
    letter-spacing: 2px;
    color: var(--brand-blue);
  }
  .product-cn {
    position: absolute; top: 212px; left: 0; width: 100%;
    text-align: center;
    font-family: 'Noto Sans SC', sans-serif;
    font-weight: 500; font-size: 38px; letter-spacing: 1px;
  }
  .claim-band {
    position: absolute; top: 296px; left: 0; width: 100%; height: 256px;
    background: linear-gradient(90deg, var(--band-shade) 0%, var(--band-blue) 12%, var(--band-blue) 88%, #9fd5ee 97%, var(--band-blue) 100%);
    color: var(--white); text-align: center;
  }
  .claim-kicker {
    position: absolute; left: 0; width: 100%;
    font-size: 28px; font-weight: 400; letter-spacing: 1px;
  }
  .claim-kicker.deep { top: 14px; }
  .claim-kicker.lasting { top: 128px; font-size: 26px; }
  .claim-script {
    position: absolute; left: 0; width: 100%;
    font-family: 'Yellowtail', cursive;
    font-size: 84px; line-height: 1;
  }
  .claim-script.cleaning { top: 40px; }
  .claim-script.freshness { top: 152px; font-size: 92px; }
  .claim-amp {
    position: absolute; top: 110px; left: 0; width: 100%;
    font-family: 'Yellowtail', cursive; font-size: 20px;
  }
  .flavor-tag {
    position: absolute; top: 612px; left: 86px;
    display: flex; align-items: center;
  }
  .flavor-leaf {
    width: 84px; height: 84px; border-radius: 50%;
    background: radial-gradient(circle at 45% 45%, var(--leaf), #2f8a33);
    border: 3px solid #ffffff;
    box-shadow: 0 0 0 2px #cfd6d2;
    position: relative; z-index: 2;
  }
  .flavor-pill {
    margin-left: -22px; height: 52px; padding: 0 22px 0 38px;
    border-radius: 26px;
    background: linear-gradient(180deg, var(--mint), var(--mint-dark));
    color: var(--white); font-size: 25px; line-height: 52px;
  }
  .volume {
    position: absolute; top: 720px; left: 0; width: 100%;
    text-align: center; font-size: 37px; font-weight: 400;
  }
</style>
</head>
<body>
  <main class="canvas">
    <section class="label">
      <div class="brand-name">Feyla</div>
      <div class="product-cn">隐形牙套清洁泡沫</div>

      <div class="claim-band">
        <div class="claim-kicker deep">DEEP</div>
        <div class="claim-script cleaning">Cleaning</div>
        <div class="claim-amp">&amp;</div>
        <div class="claim-kicker lasting">LASTING</div>
        <div class="claim-script freshness">Freshness</div>
      </div>

      <div class="flavor-tag">
        <div class="flavor-leaf" role="img" aria-label="Mint leaves illustration"></div>
        <div class="flavor-pill">Mint Flavor</div>
      </div>

      <div class="volume">1.69 Fl Oz / 50ml</div>
    </section>
  </main>
</body>
</html>
```